Bifold for voip company

Bifold for cloud voip company

Target Market(s)

Business owners

Industry/Entity Type

Software Developer

Colors

Designer to choose colors to be used in the design.

Requirements
Must have
• Modern clean design,
• will provide content to design winner

```html
<!DOCTYPE html>
<html lang="en">
<head>
<meta charset="utf-8">
<title>Nimbvox Bifold</title>
<link href="https://fonts.googleapis.com/css2?family=Rubik:wght@300;400;500;700;900&family=Open+Sans:wght@400;600;700&display=swap" rel="stylesheet">
<style>
:root{
  --purple:#4b2b80;
  --purple-deep:#3a1f6e;
  --cyan:#1aa6df;
  --ink:#222;
  --grey-text:#555;
  --panel-left:#f1f1f3;
  --panel-right:#fafafa;
  --stage:#4d4d4d;
  --line:#d9d9de;
}
*{margin:0;padding:0;box-sizing:border-box}
html,body{width:880px;height:1200px;overflow:hidden}
body{background:var(--stage);font-family:"Open Sans",sans-serif;color:var(--ink);position:relative}
.spread{position:absolute;left:54px;width:771px;overflow:hidden;box-shadow:0 6px 0 rgba(0,0,0,.35)}
.spread--outside{top:38px;height:544px;background:var(--panel-right)}
.spread--inside{top:618px;height:540px;background:var(--panel-right)}
.abs{position:absolute}
.heading{font-family:"Rubik",sans-serif;font-weight:300;font-size:12.5px;letter-spacing:.2px;color:#333;text-transform:uppercase}
.heading b{font-weight:700;color:var(--purple)}
.heading--light{color:#fff}
.heading--light b{color:var(--cyan)}
.rule{width:18px;height:2px;background:var(--cyan);margin-top:5px}

/* outside spread */
.panel-back{left:0;top:0;width:396px;height:544px;background:var(--panel-left)}
.ghost-diamond{background:#e4e4e8;transform:rotate(45deg);border-radius:30px}
.hero-photo{left:280px;top:54px;width:348px;height:348px;transform:rotate(45deg);border-radius:44px;
  background:radial-gradient(circle at 55% 40%,#3a8fa0 0%,#1d4f66 35%,#0f2238 70%,#0a1424 100%)}
.purple-wedge{left:0;top:346px}
.partners{left:35px;top:43px}
.partner-grid{left:36px;top:72px;width:200px}
.partner{position:absolute;width:90px;height:36px;border:2px solid #cfcfd6;background:#fff;display:flex;align-items:center;justify-content:center;
  font-family:"Rubik",sans-serif;font-weight:500;font-size:13px;color:var(--purple)}
.partner::before{content:"";width:7px;height:7px;border-radius:50%;background:var(--cyan);margin-right:5px}
.clients{left:35px;top:225px}
.client-badge{position:absolute;width:38px;height:38px;border-radius:50%;background:#fff;border:2px solid #dadae0}
.address{left:128px;top:388px}
.addr-block{position:absolute;font-size:6.4px;color:var(--grey-text);line-height:1.45}
.addr-title{font-family:"Rubik",sans-serif;font-weight:500;font-size:8.5px;color:var(--purple);letter-spacing:.3px;margin-bottom:4px}
.addr-line{display:flex;gap:4px}
.addr-line svg{flex:none;margin-top:1px}
.contact-row{display:flex;align-items:center;gap:5px;font-size:6.4px;color:#333;margin-bottom:4px}
.open-hours{font-family:"Rubik",sans-serif;font-weight:700;font-size:12px;color:#111}
.open-hours span{color:var(--purple)}
.open-hours small{font-weight:400;font-size:7px}
.open-note{font-family:"Rubik",sans-serif;font-weight:500;font-size:5.6px;color:#111;letter-spacing:.2px}
.web{display:flex;align-items:center;gap:5px;font-size:9px;color:#333;white-space:nowrap}
.web b{color:var(--purple)}
.web-rule{flex:1;height:1px;background:var(--purple);position:relative;margin-left:14px}
.web-rule::before{content:"";position:absolute;left:-2px;top:-2px;width:5px;height:5px;border-radius:50%;background:var(--purple)}
.brand{right:24px;top:44px;display:flex;align-items:center;gap:8px}
.brand-dot{width:36px;height:36px;border-radius:50%;background:var(--purple)}
.brand-name{font-family:"Rubik",sans-serif;font-weight:500;font-size:26px;letter-spacing:1px;color:#333}
.tagline{right:27px;top:365px;text-align:right;font-family:"Rubik",sans-serif}
.tagline .t1{font-weight:300;font-size:22px;color:#222;letter-spacing:.5px}
.tagline .t2{font-weight:700;font-size:35px;color:var(--purple);line-height:1}
.tagline .t3{font-weight:700;font-size:23px;color:var(--purple);line-height:1.1;letter-spacing:.3px}
.tagline .bar{width:28px;height:2px;background:#333;margin:7px 0 6px auto}
.tagline .t4{font-weight:300;font-size:15px;color:#222;line-height:1.4}
.tagline .t4 b{font-weight:700;color:var(--cyan);letter-spacing:.5px}
.swoosh{right:0;bottom:0}

/* inside spread */
.devices-photo{left:0;top:0;width:396px;height:240px;
  background:radial-gradient(circle at 60% 45%,#4fc2d6 0%,#1e8cab 45%,#0f5f86 100%)}
.offer-band{left:0;top:240px;width:396px;height:116px;background:linear-gradient(90deg,#2a4ea0,#43308a 60%,#4b2b80)}
.offer{position:absolute;width:120px;text-align:center;color:#fff}
.offer-icon{width:51px;height:51px;margin:0 auto;display:block}
.offer h3{font-family:"Rubik",sans-serif;font-weight:500;font-size:10.5px;margin-top:10px;letter-spacing:.2px}
.offer p{font-size:6.3px;line-height:1.4;margin-top:8px;opacity:.92}
.features-panel{left:396px;top:0;width:375px;height:356px;background:linear-gradient(160deg,#3a3e96 0%,#3d3290 50%,#43308a 100%)}
.features-title{left:422px;top:37px}
.features-title .heading{font-size:16px}
.feature{position:absolute;width:112px;color:#fff}
.feature h4{font-family:"Rubik",sans-serif;font-weight:500;font-size:7.4px;letter-spacing:.3px;margin-bottom:7px;white-space:nowrap}
.feature p{font-size:5.6px;line-height:1.45;opacity:.85;width:100px}
.f-icon{position:absolute;width:35px;height:35px;border-radius:50%;border:1px solid rgba(255,255,255,.55);display:flex;align-items:center;justify-content:center}
.plan{left:34px;top:384px}
.plan .heading{font-size:16px}
.table-title{font-family:"Rubik",sans-serif;font-weight:700;font-size:10px;color:#111;position:absolute;letter-spacing:.2px}
.price-row{position:absolute;height:17px;display:flex;border:1px solid var(--cyan);background:#fff}
.price-row .k{font-family:"Rubik",sans-serif;font-weight:500;font-size:7.6px;padding-left:12px;display:flex;align-items:center;width:76px;color:#111}
.price-row .v{flex:1;background:var(--cyan);color:#fff;font-family:"Rubik",sans-serif;font-weight:500;font-size:7.6px;display:flex;align-items:center;padding-left:4px}
.addon-row{position:absolute;height:17px;display:flex;border:1px solid #333;background:#fff}
.addon-row .k{width:72px;font-family:"Rubik",sans-serif;font-weight:500;font-size:5.3px;padding-left:9px;display:flex;align-items:center;line-height:1.1;color:#111}
.addon-row .v{flex:1;background:#3b3b3b;color:#fff;font-family:"Rubik",sans-serif;font-weight:500;font-size:5.2px;display:flex;align-items:center;padding-left:10px;line-height:1.1}
.services{left:422px;top:380px;width:318px}
.services .heading{font-size:16px}
.service{position:absolute;left:0;width:318px}
.service h4{font-family:"Rubik",sans-serif;font-weight:500;font-size:8.8px;color:var(--purple);letter-spacing:.3px;margin-bottom:4px}
.service p{font-size:5.4px;line-height:1.5;color:#333}
</style>
</head>
<body>

<section class="spread spread--outside">
  <div class="abs panel-back"></div>
  <div class="abs ghost-diamond" style="left:285px;top:-150px;width:260px;height:260px"></div>
  <div class="abs ghost-diamond" style="left:520px;top:-120px;width:150px;height:150px;background:#ececef"></div>

  <svg class="abs purple-wedge" width="120" height="198" viewBox="0 0 120 198">
    <path d="M0 0 L100 98 Q112 110 100 122 L24 198 L0 198 Z" fill="var(--purple)"/>
  </svg>

  <svg class="abs swoosh" width="230" height="160" viewBox="0 0 230 160">
    <path d="M230 0 L230 160 L20 160 Q150 130 200 40 Q215 10 230 0 Z" fill="#e6e6ea"/>
  </svg>

  <div class="abs hero-photo" role="img" aria-label="Photo of a hand holding a tablet with glowing cloud network diagram over a server room"></div>

  <div class="abs partners">
    <div class="heading">Our <b>Partners</b></div>
    <div class="rule"></div>
  </div>
  <div class="abs partner-grid">
    <div class="partner" style="left:0;top:0">Brightpath</div>
    <div class="partner" style="left:104px;top:0">Linkwave</div>
    <div class="partner" style="left:0;top:41px">Tallyo</div>
    <div class="partner" style="left:104px;top:41px">Billnest</div>
    <div class="partner" style="left:0;top:83px">Deskora</div>
  </div>

  <div class="abs clients">
    <div class="heading">Our <b>Clients</b></div>
    <div class="rule"></div>
  </div>
  <div class="client-badge" style="left:34px;top:257px"></div>
  <div class="client-badge" style="left:80px;top:257px"></div>
  <div class="client-badge" style="left:34px;top:305px"></div>
  <div class="client-badge" style="left:80px;top:305px"></div>
  <div class="client-badge" style="left:125px;top:305px"></div>
  <div class="client-badge" style="left:171px;top:305px"></div>

  <div class="abs address">
    <div class="heading">Our <b>Address</b></div>
    <div class="rule"></div>
  </div>
  <div class="addr-block" style="left:128px;top:421px;width:120px">
    <div class="addr-title">TECHNICAL SERVICES :</div>
    <div class="addr-line">
      <svg width="6" height="8" viewBox="0 0 6 8"><path d="M3 0a3 3 0 0 1 3 3c0 2-3 5-3 5S0 5 0 3a3 3 0 0 1 3-3z" fill="var(--cyan)"/></svg>
      <span>48 Harbor Way Bldg C,<br>Suite 12 Millbrook, NJ 07100</span>
    </div>
  </div>
  <div class="addr-block" style="left:128px;top:465px;width:125px">
    <div class="addr-title">BILLING DEPARTMENT :</div>
    <div class="addr-line">
      <svg width="6" height="8" viewBox="0 0 6 8"><path d="M3 0a3 3 0 0 1 3 3c0 2-3 5-3 5S0 5 0 3a3 3 0 0 1 3-3z" fill="var(--cyan)"/></svg>
      <span>910 Elm Avenue N. Cedar Bay,<br>FL 33000</span>
    </div>
  </div>
  <div class="abs" style="left:262px;top:422px">
    <div class="contact-row"><svg width="7" height="5" viewBox="0 0 7 5"><rect x=".5" y=".5" width="6" height="4" fill="none" stroke="var(--cyan)"/><path d="M.5.5l3 2 3-2" fill="none" stroke="var(--cyan)"/></svg>hello@nimbvox.example</div>
    <div class="contact-row"><svg width="6" height="6" viewBox="0 0 6 6"><circle cx="3" cy="3" r="2.5" fill="none" stroke="var(--cyan)"/></svg>1-800-Nimbvox</div>
    <div class="contact-row"><svg width="6" height="6" viewBox="0 0 6 6"><path d="M1 0h1.5l.5 1.5-1 .8a4 4 0 0 0 1.7 1.7l.8-1L6 3.5V5c0 .5-.5 1-1 1A5 5 0 0 1 0 1c0-.5.5-1 1-1z" fill="var(--cyan)"/></svg>555-014-2280</div>
    <div class="contact-row" style="margin-top:10px"><svg width="6" height="6" viewBox="0 0 6 6"><circle cx="3" cy="3" r="2.5" fill="none" stroke="var(--cyan)"/><path d="M3 1.5V3h1.2" fill="none" stroke="var(--cyan)" stroke-width=".7"/></svg>Mon-Fri: 8:30 AM - 5 PM EST</div>
    <div class="open-hours">OPEN <span>24X7</span> <small>FOR</small></div>
    <div class="open-note">SERVICE IMPACTING ISSUES</div>
  </div>

  <div class="abs web" style="left:120px;top:516px;width:276px">
    <svg width="9" height="9" viewBox="0 0 10 10"><circle cx="5" cy="5" r="4.3" fill="none" stroke="var(--cyan)"/><ellipse cx="5" cy="5" rx="1.8" ry="4.3" fill="none" stroke="var(--cyan)"/><path d="M.7 5h8.6" stroke="var(--cyan)"/></svg>
    <span>www.<b>nimbvox</b>.example</span>
    <span class="web-rule"></span>
  </div>

  <div class="abs web" style="left:432px;top:516px;width:339px;font-size:10px">
    <svg width="10" height="10" viewBox="0 0 10 10"><circle cx="5" cy="5" r="4.3" fill="none" stroke="var(--cyan)"/><ellipse cx="5" cy="5" rx="1.8" ry="4.3" fill="none" stroke="var(--cyan)"/><path d="M.7 5h8.6" stroke="var(--cyan)"/></svg>
    <span>www.<b>nimbvox</b>.example</span>
    <span class="web-rule"></span>
  </div>

  <div class="abs brand">
    <div class="brand-dot"></div>
    <div class="brand-name">NIMBVOX</div>
  </div>

  <div class="abs tagline">
    <div class="t1">REDEFINING</div>
    <div class="t2">CLOUD</div>
    <div class="t3">COMMUNICATION</div>
    <div class="bar"></div>
    <div class="t4">Work from the <b>OFFICE, HOME</b><br>or on the road.</div>
  </div>
</section>

<section class="spread spread--inside">
  <div class="abs devices-photo" role="img" aria-label="Illustration of a desk phone, smartphone, laptop and monitor showing a phone system portal on a teal network background"></div>
  <div class="abs offer-band"></div>

  <div class="offer" style="left:33px;top:218px">
    <svg class="offer-icon" viewBox="0 0 52 52"><circle cx="26" cy="26" r="25" fill="#fff" stroke="var(--cyan)" stroke-width="1.5"/><circle cx="26" cy="26" r="15" fill="none" stroke="var(--cyan)" stroke-width="2"/><circle cx="26" cy="26" r="4" fill="none" stroke="var(--cyan)" stroke-width="2"/></svg>
    <h3>HOSTED PBX</h3>
    <p>Innovative features,<br>geo-redundant network,<br>jaw dropping price.</p>
  </div>
  <div class="offer" style="left:142px;top:218px">
    <svg class="offer-icon" viewBox="0 0 52 52"><circle cx="26" cy="26" r="25" fill="#fff" stroke="var(--cyan)" stroke-width="1.5"/><circle cx="26" cy="26" r="18" fill="none" stroke="var(--cyan)" stroke-width="2"/><circle cx="26" cy="26" r="13" fill="none" stroke="var(--cyan)" stroke-width="2"/><circle cx="26" cy="26" r="8" fill="none" stroke="var(--cyan)" stroke-width="2"/><circle cx="26" cy="26" r="3" fill="var(--cyan)"/></svg>
    <h3>SIP TRUNKING</h3>
    <p>Not ready to give up your<br>current phone system? Leverage<br>the cloud for your phone service<br>and integrate seamlessly.</p>
  </div>
  <div class="offer" style="left:260px;top:218px">
    <svg class="offer-icon" viewBox="0 0 52 52"><circle cx="26" cy="26" r="25" fill="#fff" stroke="var(--cyan)" stroke-width="1.5"/><circle cx="26" cy="26" r="18" fill="none" stroke="var(--cyan)" stroke-width="3"/><circle cx="26" cy="26" r="12" fill="none" stroke="var(--cyan)" stroke-width="3"/><circle cx="26" cy="26" r="6" fill="none" stroke="var(--cyan)" stroke-width="3"/></svg>
    <h3>RESELLER PROGRAMS</h3>
    <p>Interested in selling,<br>installing, and managing<br>Hosted PBX? You came to the<br>right place.</p>
  </div>

  <div class="abs features-panel"></div>
  <div class="abs features-title">
    <div class="heading heading--light">Some of our <b>Innovative Features</b></div>
    <div class="rule"></div>
  </div>

  <div class="f-icon" style="left:422px;top:83px"><svg width="16" height="16" viewBox="0 0 16 16" fill="none" stroke="#fff"><circle cx="8" cy="8" r="3"/><circle cx="8" cy="8" r="6" stroke-dasharray="2 1.5"/></svg></div>
  <div class="feature" style="left:470px;top:80px"><h4>AUTOMATED ATTENDANTS</h4><p>Automatically greet callers and route them anywhere. Easily customizable through the web portal.</p></div>

  <div class="f-icon" style="left:592px;top:83px"><svg width="16" height="16" viewBox="0 0 16 16" fill="none" stroke="#fff"><path d="M3 9V7a5 5 0 0 1 10 0v2"/><rect x="2" y="8" width="3" height="4" fill="#fff"/><rect x="11" y="8" width="3" height="4" fill="#fff"/></svg></div>
  <div class="feature" style="left:640px;top:80px"><h4>CALL CENTER</h4><p>Setup call queues for offices with longer than normal hold times. Comes with detailed reporting.</p></div>

  <div class="f-icon" style="left:422px;top:153px"><svg width="16" height="16" viewBox="0 0 16 16" fill="none" stroke="#fff"><rect x="1" y="1" width="6" height="6"/><rect x="9" y="1" width="6" height="6"/><rect x="1" y="9" width="6" height="6"/><rect x="9" y="9" width="6" height="6"/></svg></div>
  <div class="feature" style="left:470px;top:143px"><h4>MOBILE APP</h4><p>Make and receive calls on the road just like you are in the office. Also adjust your out of office answering rules, check if co-workers are on a call, and more right from the app.</p></div>

  <div class="f-icon" style="left:592px;top:153px"><svg width="16" height="16" viewBox="0 0 16 16" fill="none" stroke="#fff"><rect x="5" y="1" width="7" height="14" rx="1"/><path d="M7.5 13h2"/></svg></div>
  <div class="feature" style="left:640px;top:155px"><h4>MOBILE TWINNING</h4><p>Simultaneously ring your cell phone with your desk phone.</p></div>

  <div class="f-icon" style="left:422px;top:221px"><svg width="16" height="16" viewBox="0 0 16 16" fill="none" stroke="#fff"><path d="M6 14V5a1 1 0 0 1 2 0v5l4 1v3"/><path d="M4 5a3 3 0 0 1 6 0"/></svg></div>
  <div class="feature" style="left:470px;top:222px"><h4>MUSIC ON HOLD</h4><p>Use our standard music on hold or upload your own.</p></div>

  <div class="f-icon" style="left:592px;top:221px"><svg width="16" height="16" viewBox="0 0 16 16" fill="none" stroke="#fff"><path d="M2 7c0-3 3-5 6-5s6 2 6 5-3 5-6 5l-4 2 1-3c-2-1-3-2-3-4z"/></svg></div>
  <div class="feature" style="left:640px;top:222px"><h4>CONFERENCE BRIDGES</h4><p>Hold password protected, multi-party conference calls.</p></div>

  <div class="f-icon" style="left:422px;top:283px"><svg width="16" height="16" viewBox="0 0 16 16" fill="none" stroke="#fff"><rect x="1" y="2" width="14" height="9"/><path d="M6 14h4M8 11v3"/></svg></div>
  <div class="feature" style="left:470px;top:278px"><h4>WEB PORTAL WITH CHAT</h4><p>Chat with coworkers, see if they are on the phone, view your call history or make system changes right from our easy to use portal.</p></div>

  <div class="f-icon" style="left:592px;top:283px"><svg width="16" height="16" viewBox="0 0 16 16" fill="none" stroke="#fff"><path d="M3 2h2l1 3-1.5 1a7 7 0 0 0 4 4l1-1.5 3 1v2c0 1-1 2-2 2A11 11 0 0 1 1 4c0-1 1-2 2-2z"/><rect x="10" y="1" width="5" height="3.5"/></svg></div>
  <div class="feature" style="left:640px;top:278px"><h4>VOICEMAIL TO EMAIL</h4><p>Have voicemails delivered right to your email, complete with caller id, .wav file, and a full text transcription of the voicemail.</p></div>

  <div class="abs plan">
    <div class="heading">Introducing <b>Unlimited Plan</b></div>
    <div class="rule"></div>
  </div>
  <div class="table-title" style="left:34px;top:424px">UNLIMITED PLAN</div>
  <div class="price-row" style="left:34px;top:442px;width:149px"><span class="k">1 User</span><span class="v">$29.99 /month</span></div>
  <div class="price-row" style="left:34px;top:464px;width:149px"><span class="k">2 - 10 Users</span><span class="v">$24.99 /month</span></div>
  <div class="price-row" style="left:34px;top:486px;width:149px"><span class="k">11 - 49 Users</span><span class="v">$21.99 /month</span></div>
  <div class="price-row" style="left:34px;top:508px;width:149px"><span class="k">50+ Users</span><span class="v">CONTACT US</span></div>

  <div class="table-title" style="left:202px;top:424px">ADD ONS</div>
  <div class="addon-row" style="left:202px;top:442px;width:149px"><span class="k">Call Recording:</span><span class="v">Starting $5 /user</span></div>
  <div class="addon-row" style="left:202px;top:464px;width:149px"><span class="k">Additional<br>Local Numbers:</span><span class="v">Starting $1.99 /number</span></div>
  <div class="addon-row" style="left:202px;top:486px;width:149px"><span class="k">Fax to Email:</span><span class="v">Starting $8 /user</span></div>
  <div class="addon-row" style="left:202px;top:508px;width:149px"><span class="k">Toll Free Numbers:</span><span class="v">Starting $1.99 /number<br>+ usage</span></div>

  <div class="abs services" style="height:150px">
    <div class="heading">Our <b>Services</b></div>
    <div class="rule"></div>
    <div class="service" style="top:33px"><h4>VOICE &amp; DATA WIRING</h4><p>Our technicians can provide certified in office wiring for your employee workstations. Call today to have us survey your project for Cat5e or Cat6 wiring. This wiring is necessary for your telephones and computers to work. We can upgrade your existing, outdated wiring or start a brand new project in your new location.</p></div>
    <div class="service" style="top:81px"><h4>FIBER</h4><p>Whether trying to extend a data network passed the recommended 300ft, or looking for the faster speeds of a fiber network, our trained technicians can make this project smooth and efficient.</p></div>
    <div class="service" style="top:121px"><h4>SOUND SOLUTIONS</h4><p>Our trained technicians specialize in office sound systems. Call us today to schedule an appointment with a sound specialist to create a more comfortable environment in your workspace.</p></div>
  </div>
</section>

</body>
</html>
```